I dont have a logo yet. My mind in color is navy blue and khaki maybe a tiny bit of yellow but open to ideas. name of the business is Granite Ridge Builders. Dedicated to all sorts of construction commerical and residential. Im Tomas Vantrell owner of business<br/>Address to business is 862 N. Berrymoor Marlow Bend NM 88042 <br/>Phone is 5055827143<br/>Id like round corners i also like the see thru card a little.<br/>Open to trademark quotes

Target Market(s)

Construction

Contact Information for Business Card

GRANITE RIDGE BUILDERS LLC

Tomas Vantrell
Director of Operations

Commercial & Residential

5055827143
GRANITE.R.BUILDERS@QUORVANMAIL.COM

Colors
0355a3
fff3d1

Requirements
Must have
• ROUND CORNERS
• BLUE AND KHAKI AND CLEAR
• LOGO

```html
<!DOCTYPE html>
<html lang="en">
<head>
<meta charset="utf-8">
<title>Granite Ridge Builders – Business Card</title>
<link rel="stylesheet" href="https://fonts.googleapis.com/css2?family=Poppins:wght@300;400;600&display=swap">
<style>
  :root {
    --navy: #1f45a0;
    --khaki: #f3dca0;
    --grey-text: #7d7d7d;
    --ink: #3a3a3a;
    --card: #ffffff;
    --backdrop: #e9e9ea;
  }
  * { box-sizing: border-box; margin: 0; padding: 0; }
  html, body { width: 1200px; height: 675px; overflow: hidden; }
  body {
    background: var(--backdrop);
    font-family: "Poppins", sans-serif;
    display: flex;
    align-items: center;
    justify-content: center;
    gap: 44px;
  }
  .card {
    width: 520px;
    height: 298px;
    background: var(--card);
    border-radius: 14px;
    box-shadow: 0 6px 18px rgba(0,0,0,0.18);
    position: relative;
  }

  /* Front */
  .card--front {
    display: flex;
    align-items: center;
    justify-content: center;
  }
  .brand { display: flex; flex-direction: column; align-items: flex-start; }
  .brand__row { display: flex; align-items: center; gap: 10px; }
  .brand__mark {
    width: 14px;
    height: 14px;
    background: var(--khaki);
    flex: none;
  }
  .brand__name {
    font-family: "Poppins", sans-serif;
    font-weight: 600;
    font-size: 24px;
    line-height: 1.1;
    color: var(--navy);
    white-space: nowrap;
  }
  .brand__tagline {
    font-family: "Poppins", sans-serif;
    font-weight: 300;
    font-size: 15px;
    letter-spacing: 1.5px;
    color: var(--grey-text);
    white-space: nowrap;
    margin: 6px 0 0 24px;
  }

  /* Back */
  .card--back {
    display: flex;
    align-items: center;
    padding-left: 104px;
  }
  .person { text-align: right; }
  .person__name {
    font-weight: 600;
    font-size: 17px;
    color: var(--navy);
    text-transform: uppercase;
    white-space: nowrap;
  }
  .person__role {
    font-size: 11px;
    color: var(--ink);
    margin-top: -2px;
  }
  .divider {
    width: 2px;
    height: 58px;
    background: var(--khaki);
    margin: 0 16px;
  }
  .contact { list-style: none; }
  .contact__item {
    display: flex;
    align-items: center;
    gap: 6px;
    font-size: 10.5px;
    color: var(--ink);
    line-height: 1.65;
    white-space: nowrap;
  }
  .contact__icon { width: 10px; height: 10px; fill: var(--navy); flex: none; }
</style>
</head>
<body>
  <section class="card card--front">
    <div class="brand">
      <div class="brand__row">
        <span class="brand__mark"></span>
        <span class="brand__name">Granite Ridge Builders</span>
      </div>
      <div class="brand__tagline">Commercial and Residential</div>
    </div>
  </section>

  <section class="card card--back">
    <div class="person">
      <div class="person__name">Tomas Vantrell</div>
      <div class="person__role">Owner</div>
    </div>
    <div class="divider"></div>
    <ul class="contact">
      <li class="contact__item">
        <svg class="contact__icon" viewBox="0 0 24 24" aria-hidden="true"><path d="M6.6 10.8c1.4 2.8 3.8 5.1 6.6 6.6l2.2-2.2c.3-.3.7-.4 1-.2 1.1.4 2.3.6 3.6.6.6 0 1 .4 1 1V20c0 .6-.4 1-1 1C10.6 21 3 13.4 3 4c0-.6.4-1 1-1h3.5c.6 0 1 .4 1 1 0 1.3.2 2.5.6 3.6.1.3 0 .7-.2 1z"/></svg>
        5055827143
      </li>
      <li class="contact__item">
        <svg class="contact__icon" viewBox="0 0 24 24" aria-hidden="true"><path d="M2 5h20v14H2z M4 7v.5l8 5 8-5V7l-8 5z" fill-rule="evenodd"/></svg>
        info@youremail.com
      </li>
      <li class="contact__item">
        <svg class="contact__icon" viewBox="0 0 24 24" aria-hidden="true"><path d="M12 2a7 7 0 0 0-7 7c0 5.2 7 13 7 13s7-7.8 7-13a7 7 0 0 0-7-7zm0 9.5A2.5 2.5 0 1 1 12 6.5a2.5 2.5 0 0 1 0 5z"/></svg>
        862 N. Berrymoor Marlow Bend NM 88042
      </li>
    </ul>
  </section>
</body>
</html>
```